General Contractors need a new Crisp updated Card Design

We need a new business card design for our company of 25 years based in Toronto call Holvaster Building Inc. : Our goal is to be the leading commercial contractors in Toronto by providing exceptional value to our clients. We work very hard to deliver professional, quality, service in conjunction with consistent price competitiveness to all of our clients on every single project.

Target Market(s)

Design & Build Clients

Industry/Entity Type

Construction Company

Contact Information for Business Card

Address:
18 North Tamlin Glen Road, Unit 57, Marbrook Vale, ON, K7T 2R9
Office: 905-218-5937

Holvasters Logo
Employee Job Description
Employee Cell Phone #
Employee Email
www.holvaster-example.com

Colors

Designer to choose colors to be used in the design.

Requirements
Must have
• Quote Company Saying:
• "Professional. Quality. Service."
Nice to have
• New Crisp up to date look. simple & fresh ( Not to Busy)
Should not have
• NO BLUE PRINTS ON THE BUSINESS CARDS

```html
<!DOCTYPE html>
<html lang="en">
<head>
<meta charset="utf-8">
<title>Holvaster Building Inc. — Business Card</title>
<link rel="stylesheet" href="https://fonts.googleapis.com/css2?family=Montserrat:wght@400;500;700;800&family=Libre+Baskerville:ital@1&display=swap">
<style>
  :root {
    --green: #12c24f;
    --green-deep: #0a9f3b;
    --ink: #1f1f1f;
    --paper: #ffffff;
    --backdrop: #c9cbcd;
    --text-font: "Montserrat", Arial, sans-serif;
    --address-font: "Libre Baskerville", Georgia, serif;
  }
  * { box-sizing: border-box; margin: 0; padding: 0; }
  html, body { width: 1200px; height: 857px; overflow: hidden; }
  body {
    background: var(--backdrop);
    font-family: var(--text-font);
    display: flex;
    align-items: center;
    justify-content: center;
    gap: 50px;
  }
  .card {
    width: 525px;
    height: 300px;
    position: relative;
    box-shadow: 0 2px 6px rgba(0,0,0,.15);
  }

  /* Front */
  .card--front {
    background: linear-gradient(135deg, var(--green) 0%, var(--green-deep) 100%);
    color: var(--paper);
    display: flex;
    flex-direction: column;
    align-items: center;
    justify-content: center;
  }
  .brand { display: flex; align-items: center; gap: 14px; }
  .brand__mark { width: 54px; height: 54px; background: var(--paper); flex: none; }
  .brand__name {
    font-weight: 700;
    font-size: 26px;
    line-height: 1.05;
    letter-spacing: 1px;
    text-transform: uppercase;
  }
  .tagline {
    margin-top: 16px;
    font-weight: 700;
    font-size: 13px;
    letter-spacing: 1.5px;
    text-transform: uppercase;
  }

  /* Back */
  .card--back { background: var(--paper); color: var(--ink); }
  .back__company {
    position: absolute;
    left: 26px;
    top: 118px;
    width: 200px;
  }
  .brand--small { gap: 8px; }
  .brand--small .brand__mark { width: 24px; height: 24px; background: var(--green); }
  .brand--small .brand__name { font-size: 13px; color: var(--green); letter-spacing: .5px; }
  .address {
    margin-top: 12px;
    font-family: var(--address-font);
    font-style: italic;
    font-size: 10.5px;
    line-height: 1.45;
  }
  .divider {
    position: absolute;
    left: 238px;
    top: 40px;
    width: 2px;
    height: 220px;
    background: var(--green);
  }
  .person {
    position: absolute;
    right: 30px;
    top: 38px;
    text-align: right;
  }
  .person__name {
    font-weight: 800;
    font-size: 24px;
    letter-spacing: 2px;
    color: var(--green);
    text-transform: uppercase;
  }
  .person__role { font-size: 15px; font-weight: 500; margin-top: 2px; }
  .person__rule {
    display: block;
    margin: 4px 0 0 auto;
    width: 40px;
    height: 2px;
    background: var(--green);
  }
  .contacts {
    position: absolute;
    left: 262px;
    top: 132px;
    list-style: none;
  }
  .contacts__item {
    display: flex;
    align-items: center;
    gap: 12px;
    font-size: 13.5px;
    height: 25px;
  }
  .contacts__icon { width: 14px; height: 14px; flex: none; }
</style>
</head>
<body>

  <section class="card card--front" aria-label="Business card front">
    <div class="brand">
      <span class="brand__mark"></span>
      <span class="brand__name">Holvaster<br>Building Inc.</span>
    </div>
    <p class="tagline">Professional | Quality | Service</p>
  </section>

  <section class="card card--back" aria-label="Business card back">
    <div class="back__company">
      <div class="brand brand--small">
        <span class="brand__mark"></span>
        <span class="brand__name">Holvaster Building Inc.</span>
      </div>
      <p class="address">18 North Tamlin Glen Road, Unit 57,<br>Marbrook Vale, ON, K7T 2R9</p>
    </div>

    <span class="divider"></span>

    <div class="person">
      <h1 class="person__name">Marcus Hale</h1>
      <p class="person__role">Co-Founder &amp; CEO</p>
      <span class="person__rule"></span>
    </div>

    <ul class="contacts">
      <li class="contacts__item">
        <svg class="contacts__icon" viewBox="0 0 14 14" fill="none" stroke="var(--green)" stroke-width="1.4"><rect x="3.5" y="1" width="7" height="12" rx="1.2"/><line x1="6" y1="11" x2="8" y2="11"/></svg>
        <span>905-218-5937</span>
      </li>
      <li class="contacts__item">
        <svg class="contacts__icon" viewBox="0 0 14 14" fill="var(--green)"><path d="M3 1.2l2.2 2.6-1.2 1.5c.8 1.8 2.2 3.2 4 4l1.5-1.2 2.6 2.2-1.4 2.2C6.3 12.4 1.6 7.7 1 3.1z"/></svg>
        <span>905-218-5937</span>
      </li>
      <li class="contacts__item">
        <svg class="contacts__icon" viewBox="0 0 14 14" fill="none" stroke="var(--green)" stroke-width="1.4"><rect x="1" y="3" width="12" height="8.5"/><path d="M1 3l6 5 6-5"/></svg>
        <span>info@holvaster-example.com</span>
      </li>
      <li class="contacts__item">
        <svg class="contacts__icon" viewBox="0 0 14 14" fill="none" stroke="var(--green)" stroke-width="1.3"><circle cx="7" cy="7" r="5.8"/><ellipse cx="7" cy="7" rx="2.4" ry="5.8"/><line x1="1.2" y1="7" x2="12.8" y2="7"/></svg>
        <span>www.holvaster-example.com</span>
      </li>
    </ul>
  </section>

</body>
</html>
```